Professional Accounting Services Flyer

Attached is a publisher document and word document each containing the flyer text. This needs to be polished and improved to become an A4 2 sided marketing flyer.
It would be helpful if the design graphics on the flyer are in keeping with the product being sold, which is accounting and financial services.
The business in essence provides outsourced Chief Financial Office (CFO) services along with bookkeeping and a range of other accounting functions.

Target Market(s)

Small to Medium sized businesses requiring accounting support beyond the traditional preparation of tax returns

Industry/Entity Type

Accounting

Colors
0255a3
3277b5
85acd3
cedeed
ffffff
000000

Requirements
Must have
• The provided text
• Professional look and feel consistent with provision of professional accounting and financial services
• 2 sided A4 flyer
Nice to have
• Effective graphics which enhance the message and are in keeping with the theme of the business
Should not have
• Tacky or gimmicky looking graphics (please keep the graphics professional looking)
• A feel that indicates that tax return preparation is part of the business

```html
<!DOCTYPE html>
<html lang="en">
<head>
<meta charset="utf-8">
<title>Keystone Advisory – Flyer</title>
<link href="https://fonts.googleapis.com/css2?family=Roboto:ital,wght@0,400;0,500;0,700;0,900;1,700&family=Roboto+Condensed:wght@400;500;700&display=swap" rel="stylesheet">
<style>
:root{
  --green:#0c8a0c;
  --green-dark:#076d07;
  --ink:#222;
  --charcoal:#3a3a3a;
  --backdrop:#808080;
  --white:#fff;
  --body-text:#333;
}
*{margin:0;padding:0;box-sizing:border-box}
html,body{width:1200px;height:1200px;overflow:hidden;background:var(--backdrop)}
body{font-family:"Roboto",sans-serif;color:var(--body-text)}
.stage{position:absolute;left:0;top:0;width:1400px;height:1400px;transform:scale(.857143);transform-origin:0 0}
.page{position:absolute;top:272px;width:611px;height:858px;background:var(--white);overflow:hidden}
.page--front{left:60px}
.page--back{left:743px}
.abs{position:absolute}
.tab{position:absolute;height:22px;background:var(--green);color:var(--white);font:500 12px/22px "Roboto",sans-serif;padding:0 30px 0 28px;white-space:nowrap;clip-path:polygon(0 0,100% 0,calc(100% - 14px) 100%,0 100%)}
.tab--sm{height:15px;font:500 11px/15px "Roboto",sans-serif;padding:0 14px 0 4px}
.copy{font-size:8.6px;line-height:10.6px;text-align:justify}
.checks{list-style:none}
.checks li{position:relative;padding-left:18px}
.checks svg{position:absolute;left:0;top:1px;width:10px;height:10px}
/* front */
.brand{left:32px;top:24px;font:900 30px/1 "Roboto",sans-serif;color:var(--green);letter-spacing:1px}
.phone{left:385px;top:27px;display:flex;align-items:center;gap:10px;font:500 17px/1 "Roboto",sans-serif;color:var(--ink)}
.header-rule{left:280px;top:66px;width:331px;height:6px;background:var(--ink)}
.hero-photo{left:0;top:72px;width:360px;height:305px;background:linear-gradient(135deg,#c9b27a 0%,#eae3cf 40%,#d8d4c8 70%,#f0eee8 100%)}
.hero-panel{left:290px;top:72px;width:321px;height:305px;background:var(--green);clip-path:polygon(55px 0,100% 0,100% 100%,0 100%)}
.hero-title{left:347px;top:130px;font:500 33px/40px "Roboto Condensed",sans-serif;color:var(--white);transform:scaleX(.8);transform-origin:0 0;white-space:nowrap}
.hero-strong{left:347px;top:222px;font:700 60px/54px "Roboto Condensed",sans-serif;color:#1a1a1a;transform:scaleX(.85);transform-origin:0 0}
.services-head{left:355px;top:510px;width:250px;font:500 12px/14px "Roboto",sans-serif;color:var(--green)}
.services-box{left:338px;top:540px;width:273px;height:195px;background:var(--charcoal);color:var(--white);padding:18px 16px}
.services-box .copy{text-align:left;color:#eee}
.services-box .checks{margin-top:26px;font:500 12px/21px "Roboto",sans-serif}
.services-box .checks svg{top:5px}
.secretarial-head{left:338px;top:735px;width:273px;height:20px;font:500 12px/20px "Roboto",sans-serif;color:var(--green);padding-left:16px;border-bottom:2px solid var(--charcoal)}
.secretarial-box{left:338px;top:755px;width:273px;height:88px;background:var(--charcoal);color:#eee;padding:16px 16px}
.foot-band{left:0;bottom:0;width:611px;height:15px;background:var(--green)}
/* back */
.desk-photo{left:0;top:0;width:612px;height:168px;background:linear-gradient(160deg,#4a6a88 0%,#7d95ad 35%,#c7d3dc 65%,#eef1f2 100%)}
.back-left{left:28px;top:180px;width:272px}
.back-left .copy{font-size:8.4px;line-height:10.4px}
.back-left section{margin-bottom:9px}
.back-left .tab--sm{position:relative;display:inline-block;margin-bottom:5px}
.back-left .checks{font:500 8.4px/15px "Roboto",sans-serif;color:var(--ink)}
.back-left .checks svg{top:3px;width:9px;height:9px}
.faq-panel{left:328px;top:168px;width:284px;height:584px;background:var(--green);padding:12px 22px 0 14px;color:var(--white)}
.faq-title{display:inline-block;font:500 11.5px/14px "Roboto",sans-serif;color:var(--white);border-bottom:2px solid var(--white);margin-bottom:8px;padding-right:10px}
.faq{margin-bottom:12px}
.faq h3{position:relative;padding-left:12px;font:italic 700 9.4px/11.5px "Roboto",sans-serif;margin-bottom:5px}
.faq h3 svg{position:absolute;left:0;top:1px;width:8px;height:8px}
.faq p{padding-left:12px;font-size:8.4px;line-height:10.4px;text-align:justify}
.coins-photo{left:328px;top:752px;width:284px;height:93px;background:linear-gradient(90deg,#3a2a14 0%,#8a6228 45%,#e4b04a 70%,#5a4020 100%)}
.back-band{left:0;top:845px;width:612px;height:13px;background:#0f1f0f}
</style>
</head>
<body>
<svg width="0" height="0" style="position:absolute">
  <symbol id="tick" viewBox="0 0 12 12"><circle cx="6" cy="6" r="5" fill="none" stroke="currentColor" stroke-width="1.4"/><path d="M3.4 6.2l1.8 1.8 3.6-3.8" fill="none" stroke="currentColor" stroke-width="1.5"/></symbol>
</svg>
<main class="stage">
  <article class="page page--front">
    <div class="abs brand">Keystone</div>
    <div class="abs phone">
      <svg width="22" height="22" viewBox="0 0 24 24"><circle cx="12" cy="12" r="10.5" fill="none" stroke="var(--green)" stroke-width="1.8"/><path d="M8.5 6.8l1.6-.3 1.2 2.7-1.1.9c.6 1.4 1.6 2.5 3 3.1l.9-1.1 2.7 1.2-.3 1.6c-.2.6-.8 1-1.5.9-3.7-.5-6.6-3.4-7.1-7.1-.1-.7.3-1.3.6-1.9z" fill="var(--green)"/></svg>
      <span>(01) 555 019 2834</span>
    </div>
    <div class="abs header-rule"></div>
    <div class="abs hero-photo" role="img" aria-label="Photo of an alarm clock beside stacks of coins on banknotes"></div>
    <div class="abs hero-panel"></div>
    <h1 class="abs hero-title">KEYSTONE ADVISORY<br>PROVIDES</h1>
    <div class="abs hero-strong">EXPERT<br>OPINIONS</div>

    <div class="tab" style="top:373px">ABOUT KEYSTONE ADVISORY</div>
    <p class="abs copy" style="left:28px;top:410px;width:557px">Keystone Advisory is focused on delivering services to small and medium businesses which are often only available to larger businesses. At its core Keystone Advisory is focused on providing to small and medium sized businesses the key services large organisations gain through the employment of a dedicated CFO.<br>These services will enable you to focus your efforts on growing your business and ensuring the operations are performing to achieve the goals you have set. Keystone Advisory is able to partner with you to ensure that as the business grows, the financial and governance needs continue to keep pace and enable growth to occur efficiently and effectively.<br>With growth and size comes complexity and Keystone Advisory is able assist you in managing these risks allowing the business to thrive and develop successfully.</p>

    <div class="tab" style="top:510px">WHY CHOOSE KEYSTONE ADVISORY?</div>
    <ul class="abs checks copy" style="left:28px;top:545px;width:275px;color:var(--ink);text-align:left">
      <li style="margin-bottom:8px;color:var(--green)"><svg><use href="#tick"/></svg><span style="color:var(--ink)">Are you experiencing significant growth and facing presure to continue to successfully manage all aspects of your business?</span></li>
      <li style="margin-bottom:8px;color:var(--green)"><svg><use href="#tick"/></svg><span style="color:var(--ink)">Do you find the day to day tasks of meeting your financial, accounting and company secretarial obligations is diverting your time from your core business?</span></li>
      <li style="margin-bottom:8px;color:var(--green)"><svg><use href="#tick"/></svg><span style="color:var(--ink)">Is a lack of expert financial support holding your business back from achieving its potential?</span></li>
      <li style="margin-bottom:8px;color:var(--green)"><svg><use href="#tick"/></svg><span style="color:var(--ink)">Are you considering listing, raising capital, or borrowing funds to achieve your business goals?</span></li>
      <li style="margin-bottom:8px;color:var(--green)"><svg><use href="#tick"/></svg><span style="color:var(--ink)">Are you looking for cost effective solutions to improve your business performance?</span></li>
      <li style="color:var(--green)"><svg><use href="#tick"/></svg><span style="color:var(--ink)">If this is you Keystone Advisory may be able to help you achieve these goals.</span></li>
    </ul>

    <h2 class="abs services-head">WHAT SERVICES DOES KEYSTONE ADVISORY PROVIDE?</h2>
    <div class="abs services-box">
      <p class="copy">Keystone Advisory is focused on providing outsourced solutions to your business. We specialise in the following areas.</p>
      <ul class="checks" style="color:var(--green)">
        <li><svg><use href="#tick"/></svg><span style="color:var(--white)">CFO services</span></li>
        <li><svg><use href="#tick"/></svg><span style="color:var(--white)">Company Secretarial services</span></li>
        <li><svg><use href="#tick"/></svg><span style="color:var(--white)">Financial Reporting</span></li>
        <li><svg><use href="#tick"/></svg><span style="color:var(--white)">Forensic Accounting</span></li>
        <li><svg><use href="#tick"/></svg><span style="color:var(--white)">Bookkeeping and Payroll</span></li>
      </ul>
    </div>

    <div class="tab" style="top:735px">BOOKKEEPING AND PAYROLL</div>
    <p class="abs copy" style="left:28px;top:775px;width:293px">These essential tasks form part of running every business but often take up an excessive amount of your valuable time. These tasks which are necessary can be performed by someone with the right skills allowing you to focus on the business. We can assist you with this enabling you to concentrate on the areas of your business that add the most value.</p>

    <h2 class="abs secretarial-head">COMPANY SECRETARIAL SERVICES</h2>
    <p class="abs secretarial-box copy">We can provide secretarial services whether your business is a private company just requiring the basics or if you operate a small capital listed entity requiring the services of a Company Secretary to meet the obligations of the corporate regulator as well as the National Exchange.</p>
    <div class="abs foot-band"></div>
  </article>

  <article class="page page--back">
    <div class="abs desk-photo" role="img" aria-label="Photo of hands using a calculator on a desk with papers and pens"></div>

    <div class="abs back-left">
      <section>
        <h2 class="tab tab--sm">CFO SERVICES</h2>
        <p class="copy">Large companies utilise the services of a Chief Financial Officer (CFO) to manage the financial complexity of modern businesses.</p>
        <p class="copy" style="margin-top:7px">CFO services allows you to have access to the same skills on a part time basis. This function allows you to have a senior financial professional assist with managing activities such as:</p>
        <ul class="checks" style="margin-top:5px;color:var(--green)">
          <li><svg><use href="#tick"/></svg><span style="color:var(--ink)">Strategy development and execution</span></li>
          <li><svg><use href="#tick"/></svg><span style="color:var(--ink)">Organisational structure optimisation</span></li>
          <li><svg><use href="#tick"/></svg><span style="color:var(--ink)">Insurance Management</span></li>
          <li><svg><use href="#tick"/></svg><span style="color:var(--ink)">Managing the financial team</span></li>
          <li><svg><use href="#tick"/></svg><span style="color:var(--ink)">Planning and budgeting</span></li>
          <li><svg><use href="#tick"/></svg><span style="color:var(--ink)">Debt and Capital raisings</span></li>
          <li><svg><use href="#tick"/></svg><span style="color:var(--ink)">Negotiations with financial institutions</span></li>
          <li><svg><use href="#tick"/></svg><span style="color:var(--ink)">Implementation of financial systems, policies and procedures</span></li>
        </ul>
      </section>
      <section>
        <h2 class="tab tab--sm">FORENSIC ACCOUNTING</h2>
        <p class="copy" style="width:235px">Everyone hopes their employees are honest and act with integrity, however, this is not always the case. If your business has been the subject of a suspected financial crime we can help. We can conduct a forensic review and where needed provide expert testimony should the matter lead to a court case.</p>
      </section>
      <section>
        <h2 class="tab tab--sm">KEY MANAGEMENT</h2>
        <p class="copy">Martin Hale is at the heart of the business with over 25 years of experience gained across both public practice and commerce. Most of this experience has been gained working in a range of commercial organisations ranging in size from 100 staff through to organisations with over 10,000 employees. This has included senior financial positions within top 200 listed companies with operations both within Australia and operations overseas.<br>Martin's experience extends to a range of sectors, including retailing, wholesaling, mining and exploration, construction and manufacturing. This experience is particularly extensive within fast moving consumer goods and operational mines extracting gold, copper and coal.<br>Martin has also been involved in a range of corporate activities including business acquisitions, stock exchange listings (particularly in Singapore), debt raisings and corporate demergers. Through these activities, he has been exposed to the debt and equity market regimes in Australia, Singapore and the United States of America.</p>
      </section>
      <section>
        <h2 class="tab tab--sm">FINANCIAL REPORTING</h2>
        <p class="copy" style="width:235px">Whether you need to meet the expectations of banks or outside investors we can assist by providing the necessary skills to compile financial reports.</p>
        <p class="copy" style="width:235px;margin-top:6px">Alternately you may need assistance meeting the tight deadlines associated with raising funds through debt and equity markets. We can provide this service along with assistance in the preparation of Prospectus documents or Information Memorandum. We are able to act as lead or provide supplemental support for an existing internal team.</p>
      </section>
    </div>

    <aside class="abs faq-panel">
      <h2 class="faq-title">FREQUENTLY ASKED QUESTIONS</h2>
      <div class="faq"><h3><svg><use href="#tick"/></svg>If I utilise the CFO services of Keystone Advisory, does that mean I don't need to worry about the financials?</h3><p>Keystone Advisory acts as your personal CFO. Like any successful business the CEO must remain engaged with the financial health and prosperity of the business. What Keystone Advisory will do, is assist you in fully understanding this information and using financial information to drive your business forward.</p></div>
      <div class="faq"><h3><svg><use href="#tick"/></svg>If I decide to raise capital or list my business on a stock exchange, can Keystone Advisory help me?</h3><p>Yes, there are a number of ways we can be of assistance. Keystone Advisory can act as your CFO and drive the process, including, managing the various aspects involved in raising capital and listing a company. If you already have internal resources but require additional help to achieve the outcome within the deadlines, Keystone Advisory can provide that assistance.</p></div>
      <div class="faq"><h3><svg><use href="#tick"/></svg>Does Keystone Advisory provide taxation services?</h3><p>While Keystone Advisory does not provide taxation services, we are able to assist you through an associate who is a registered tax agent.</p></div>
      <div class="faq"><h3><svg><use href="#tick"/></svg>Does Keystone Advisory conduct audit and assurance services?</h3><p>These services are not provided by Keystone Advisory, however there are a range of accounting firms we can direct you toward. We are also able to act in the same manner as a dedicated CFO would in engaging with these providers and managing the audit process should you require.</p></div>
      <div class="faq"><h3><svg><use href="#tick"/></svg>Does Keystone Advisory provide expert opinions for debt and equity raisings or takeovers?</h3><p>These are specialised services which Keystone Advisory does not provide. However, we can manage the process on your behalf to achieve the outcomes required.</p></div>
      <div class="faq"><h3><svg><use href="#tick"/></svg>Does Keystone Advisory provide Valuations?</h3><p>Keystone Advisory does not provide valuations, however, we are able to manage this process on your behalf or assist with collation of all relevant information to facilitate a valuation.</p></div>
    </aside>
    <div class="abs coins-photo" role="img" aria-label="Photo of a hand placing coins on growing stacks against a sunset"></div>
    <div class="abs back-band"></div>
  </article>
</main>
</body>
</html>
```